Create 2 X Google Templates and graphics for web portal

I would like to get a google slides 'theme' template for my business based off the company logo, this should include some images for a professional looking template. In addition a google doc template for some business documents (think FAQs, Knowledge Articles) and some images / graphics for use in a website (customer portal). This should be based on a theme using our branding colours, font and logo.

See attached brief.

```html
<!DOCTYPE html>
<html lang="en">
<head>
<meta charset="utf-8">
<title>Master Slide Presentation</title>
<link href="https://fonts.googleapis.com/css2?family=Montserrat:wght@300;400;700&display=swap" rel="stylesheet">
<style>
  :root {
    --slate: #7893a0;
    --ring: #c85c58;
    --accent: #ef4136;
    --ink: #050505;
    --white: #ffffff;
  }
  html, body {
    margin: 0;
    padding: 0;
    overflow: hidden;
  }
  .slide {
    position: relative;
    width: 1200px;
    height: 675px;
    background: var(--slate);
    overflow: hidden;
    font-family: "Montserrat", sans-serif;
  }
  .ring {
    position: absolute;
    left: 0;
    top: 0;
  }
  .brand {
    position: absolute;
    left: 360px;
    top: 97px;
    margin: 0;
    font-size: 48px;
    font-weight: 400;
    line-height: 1;
    letter-spacing: 1px;
    color: var(--white);
  }
  .title {
    position: absolute;
    left: 357px;
    top: 157px;
    margin: 0;
    font-size: 78px;
    font-weight: 700;
    line-height: 67.5px;
    letter-spacing: -0.5px;
    color: var(--ink);
  }
  .title span {
    display: block;
  }
  .subtitle {
    position: absolute;
    left: 361px;
    top: 308px;
    margin: 0;
    font-size: 30px;
    font-weight: 300;
    line-height: 1;
    color: var(--white);
  }
</style>
</head>
<body>
  <main class="slide">
    <svg class="ring" width="1200" height="675" viewBox="0 0 1200 675" aria-hidden="true">
      <path d="M562.5 355.6 A226.25 226.25 0 1 1 336.25 129.35"
            fill="none" stroke="var(--ring)" stroke-width="69.4" stroke-linecap="butt"/>
      <rect x="63" y="317" width="104" height="104" rx="9" fill="var(--accent)"/>
    </svg>
    <p class="brand">halvo</p>
    <h1 class="title"><span>Master Slide</span><span>Presentation</span></h1>
    <p class="subtitle">add here your subtitle</p>
  </main>
</body>
</html>
```